Shine4all

Full service cleaning company. Specializing in commercial and apartment cleans.
Fully licensed and insured
Digital photos and invoices provided
for every job
For web designer...basic info as expected by a highend cleaning company that provides excellent service at reasonable pricing. We are going after large property management companies as well as not pricing ourselves out to help the local mom and pop companies as well.
Updates

Project Deadline Extended Reason: Everyone seems to be having trouble understanding that we are a dumpster company that is adding a cleaning side to the company. We want our clients to see Shine4All as a separate branch of our our already established waste management company.We are not a regular cleaning company. We specialize in going after large commercial cleans and apartment cleans. I have now included info regarding a proposal for work and our invoice/job completion to make it clearer what we do Added Monday, July 20, 2015

Target Market(s)

Property Management companies in Savannah, Richmond Hill, Rincon, Hinesville and Midway Georgia

Industry/Entity Type

Cleaning Service

Coding

Coded - Design and coding required

Number of Pages Required

3 page

Requirements
Must have
• Nice home page with lots of photos (stock are fine) to convey exactly what we do (getting logo bid on right now on this sight).
• Information page with employee photos (can leave blank) need room for 4 photos and bios.
• Page or link to a static page for the dumpster company BinTrek (logo for this is red and black file attached along with photo of dumpster. This page just needs to be one page with contact info and information about commercial dumpster.
• Basically this site is just a fluff page used for marketing purposes. Its content can be general and once created wont change much. Services and photos can be provided upon request but general layout and info is what we are looking for.

```html
<!DOCTYPE html>
<html lang="en">
<head>
<meta charset="utf-8">
<title>Shine4all — Service Cleaning Company</title>
<link href="https://fonts.googleapis.com/css2?family=Oswald:wght@400;500&family=Open+Sans:wght@400;600;700&display=swap" rel="stylesheet">
<style>
:root{
  --red:#d71f26;
  --ink:#2b2b2b;
  --muted:#777;
  --light:#f1f1f1;
  --panel:#e9e9e9;
  --footer:#ececec;
  --bar:#2a2a2a;
  --white:#fff;
  --sky1:#6f8fae;
  --sky2:#c9d6e2;
}
*{box-sizing:border-box;margin:0;padding:0}
html,body{width:761px;height:1200px;overflow:hidden}
body{font-family:"Open Sans",Arial,sans-serif;color:var(--ink);background:var(--white);position:relative}

.site-header{height:78px;display:flex;align-items:center;justify-content:space-between;padding:0 40px 0 58px}
.brand{display:flex;align-items:center;gap:8px;font-family:"Open Sans",Arial,sans-serif;font-weight:700;font-size:22px;color:var(--red)}
.brand-mark{width:14px;height:14px;background:var(--red)}
.main-nav{display:flex;align-items:center;gap:18px;font-size:10px;font-weight:600;text-transform:uppercase}
.main-nav a{color:var(--ink);text-decoration:none}
.main-nav a.active{color:var(--red)}
.main-nav .login{background:var(--red);color:var(--white);padding:7px 14px;margin-left:8px}

.hero{position:relative;height:402px;background:linear-gradient(170deg,var(--sky1) 0%,var(--sky2) 45%,#7d93aa 60%,#2f5f8f 75%,#3c3f44 100%)}
.hero-text{position:absolute;left:58px;top:156px;color:var(--white)}
.hero-title{font-family:"Oswald",Arial,sans-serif;font-weight:400;font-size:25px;letter-spacing:.3px}
.hero-sub{margin-top:4px;font-size:12.5px;background:rgba(0,0,0,.25);display:inline-block;padding:2px 6px 2px 0}
.hero-arrows{position:absolute;left:58px;top:242px;display:flex;gap:3px}
.hero-arrows span{width:20px;height:20px;background:rgba(40,40,40,.75);display:flex;align-items:center;justify-content:center}

.services{display:flex;gap:28px;padding:20px 58px 0}
.service-card{width:197px}
.service-photo{height:112px;border:4px solid var(--light)}
.service-card:nth-child(1) .service-photo{background:linear-gradient(160deg,#c7c9cc,#8f959c 60%,#5c6168)}
.service-card:nth-child(2) .service-photo{background:linear-gradient(160deg,#4a86b8,#2a5f86 60%,#1f3e58)}
.service-card:nth-child(3) .service-photo{background:linear-gradient(160deg,#eef0f2,#b9c2cb 60%,#6a7480)}
.service-title{margin-top:12px;font-size:9px;font-weight:700;color:var(--red);text-transform:uppercase}
.service-text{margin-top:5px;font-size:7.5px;line-height:1.45;color:var(--muted)}

.welcome{position:absolute;top:712px;left:0;width:761px;height:205px;background:var(--panel);padding:28px 58px 0}
.welcome h2{font-family:"Oswald",Arial,sans-serif;font-weight:400;font-size:15px;text-transform:uppercase;letter-spacing:.3px}
.welcome h2 span{color:var(--red)}
.welcome-text{width:360px;margin-top:10px;font-size:8px;line-height:1.6;color:var(--muted)}
.btn-read{display:inline-block;margin-top:14px;background:var(--bar);color:var(--white);font-size:8px;padding:6px 11px;border-radius:2px}
.video{position:absolute;right:58px;top:28px;width:256px;height:160px;border:5px solid var(--white);background:linear-gradient(160deg,#5a5e63,#2a2c2f 55%,#111)}
.video-bar{position:absolute;left:0;right:0;bottom:0;height:14px;background:rgba(0,0,0,.7);display:flex;align-items:center;gap:6px;padding:0 6px}
.video-track{flex:1;height:2px;background:#888}
.video-track i{display:block;width:30%;height:2px;background:var(--red)}

.partners{position:absolute;top:945px;left:58px;right:58px;height:42px;display:flex;align-items:center;justify-content:space-between;color:#9a9a9a;font-family:"Oswald",Arial,sans-serif;font-size:17px;font-weight:500}
.partner-badge{width:48px;height:20px;background:#b5b5b5}

.site-footer{position:absolute;top:1012px;left:0;width:761px;height:133px;background:var(--footer);padding:20px 58px 0;display:flex;gap:0}
.footer-col{width:124px;font-size:7.5px;color:var(--muted);line-height:1.9}
.footer-col h3{font-size:8px;font-weight:700;color:var(--red);text-transform:uppercase;margin-bottom:6px}
.footer-col.contact{width:150px;margin-left:auto}

.bottom-bar{position:absolute;top:1145px;left:0;width:761px;height:55px;background:var(--bar);color:#bbb;font-size:7px;padding:12px 58px 0;display:flex;justify-content:space-between}
.legal p+p{margin-top:3px}
.social{display:flex;gap:4px;margin-top:2px}
.social span{width:14px;height:14px;background:#2d7fbf}
.social span:nth-child(2){background:#3b5c9a}
.social span:nth-child(3){background:#1f78b4}
.social span:nth-child(4){background:var(--red)}
</style>
</head>
<body>

<header class="site-header">
  <div class="brand"><span class="brand-mark"></span>BinTrek</div>
  <nav class="main-nav">
    <a class="active" href="#">Home</a>
    <a href="#">Bio</a>
    <a href="#">BinTrek</a>
    <a href="#">Contact Us</a>
    <a class="login" href="#">Log In</a>
  </nav>
</header>

<section class="hero" role="img" aria-label="Blue roll-off dumpster loaded on a truck under a bright cloudy sky">
  <div class="hero-text">
    <h1 class="hero-title">SERVICE CLEANING COMPANY</h1>
    <p class="hero-sub">Specializing in commercial and apartment</p>
  </div>
  <div class="hero-arrows">
    <span><svg width="8" height="8" viewBox="0 0 8 8"><path d="M5.5 1 2.5 4l3 3" stroke="#fff" stroke-width="1.4" fill="none"/></svg></span>
    <span><svg width="8" height="8" viewBox="0 0 8 8"><path d="M2.5 1 5.5 4l-3 3" stroke="#fff" stroke-width="1.4" fill="none"/></svg></span>
  </div>
</section>

<section class="services">
  <article class="service-card">
    <div class="service-photo" role="img" aria-label="Clean, bright commercial office interior"></div>
    <h3 class="service-title">Cleaning Company</h3>
    <p class="service-text">Fully licensed and insured crews working to a checklist so every site is left spotless.</p>
  </article>
  <article class="service-card">
    <div class="service-photo" role="img" aria-label="Cleaner washing large commercial windows"></div>
    <h3 class="service-title">Specializing in Commercial</h3>
    <p class="service-text">Offices, retail units and shared spaces cleaned on a schedule that fits your tenants.</p>
  </article>
  <article class="service-card">
    <div class="service-photo" role="img" aria-label="Cleaner in uniform mopping an apartment floor"></div>
    <h3 class="service-title">Apartment Cleans</h3>
    <p class="service-text">Move-out and turnover cleans with digital photos and invoices provided for every job.</p>
  </article>
</section>

<section class="welcome">
  <h2>Welcome to <span>Shine4all</span></h2>
  <p class="welcome-text">Shine4all is the cleaning branch of BinTrek, an established waste management company serving coastal Georgia. We focus on large commercial and apartment cleans for property management companies, while keeping prices fair for local family businesses. Every job ends with digital photos and an invoice, so you can see exactly what was done before you pay.</p>
  <span class="btn-read">Read More</span>
  <div class="video" role="img" aria-label="Video still of a red service truck at night">
    <div class="video-bar">
      <svg width="7" height="8" viewBox="0 0 7 8"><path d="M0 0l7 4-7 4z" fill="#fff"/></svg>
      <div class="video-track"><i></i></div>
    </div>
  </div>
</section>

<section class="partners" aria-label="Partners">
  <span>Brisko</span>
  <span>Aurelan</span>
  <span>Envoya</span>
  <span>Veranti</span>
  <span class="partner-badge"></span>
  <span>Floweth</span>
</section>

<footer class="site-footer">
  <div class="footer-col"><h3>Link</h3>About us<br>Services<br>Presentation</div>
  <div class="footer-col"><h3>Specialists</h3>Commercial<br>Residential<br>Luxury</div>
  <div class="footer-col"><h3>Advice</h3>FAQs<br>Support</div>
  <div class="footer-col"><h3>Agencies</h3>Sign Up<br>Forums<br>Promotions</div>
  <div class="footer-col contact"><h3>Contact Us</h3>418 Marsh Lane, Savannah, GA 31400<br>Phone: +1 555 014 2280<br>E-mail: hello@shine4all.example</div>
</footer>

<div class="bottom-bar">
  <div class="legal">
    <p>Privacy Policy &nbsp;|&nbsp; Terms of Use &nbsp;|&nbsp; About Us &nbsp;|&nbsp; Sitemap</p>
    <p>Copyright © 2015. All Rights</p>
  </div>
  <div class="social"><span></span><span></span><span></span><span></span></div>
</div>

</body>
</html>
```